business card for trucking industry consulting firm

Our company, Velkor Services Inc. provides numerous services to the trucking industry as listed on our website: velkor.ca
The logo i want on the card is the black and red VELKOR
update: i would like the services we provide listed on the card (see velkor.ca)

```html
<!DOCTYPE html>
<html lang="en">
<head>
<meta charset="utf-8">
<title>Velkor Services Inc. — Business Card</title>
<link href="https://fonts.googleapis.com/css2?family=Arimo:wght@400;700&display=swap" rel="stylesheet">
<style>
  :root {
    --bg: #e6eaea;
    --card: #ffffff;
    --panel: #bdbdbd;
    --ink: #1a1a1a;
    --red: #e5262b;
    --muted: #7a7a7a;
    --faint: #cfd0cf;
  }
  * { box-sizing: border-box; margin: 0; padding: 0; }
  html, body { width: 1200px; height: 900px; overflow: hidden; }
  body {
    background: var(--bg);
    font-family: "Arimo", Arial, sans-serif;
    color: var(--ink);
    display: flex;
    flex-direction: column;
    align-items: center;
    justify-content: center;
    gap: 28px;
  }
  .card {
    width: 700px;
    height: 400px;
    background: var(--card);
    position: relative;
    box-shadow: 0 2px 10px rgba(0,0,0,0.12);
    overflow: hidden;
  }

  /* Services side */
  .services { padding: 36px 34px; }
  .service-list {
    position: absolute;
    top: 36px;
    bottom: 36px;
    display: flex;
    flex-direction: column;
    justify-content: space-between;
    list-style: none;
    font-size: 17px;
    line-height: 1.2;
    z-index: 1;
  }
  .service-list--left { left: 34px; }
  .service-list--right { right: 34px; text-align: right; }
  .service-list--left li { border-left: 3px solid var(--red); padding-left: 10px; }
  .service-list--right li { border-right: 3px solid var(--red); padding-right: 10px; }
  .brand-watermark {
    position: absolute;
    left: 50%;
    top: 50%;
    transform: translate(-50%, -50%);
    text-align: center;
    color: var(--faint);
    font-weight: 700;
    line-height: 1;
  }
  .brand-watermark .brand-name { font-size: 108px; letter-spacing: 2px; }
  .brand-watermark .brand-sub { font-size: 30px; letter-spacing: 10px; margin-top: 6px; }

  /* Contact side */
  .contact { display: flex; }
  .contact-brand {
    width: 42%;
    display: flex;
    flex-direction: column;
    justify-content: center;
    align-items: center;
    font-weight: 700;
    color: var(--ink);
    line-height: 1;
  }
  .contact-brand .brand-name { font-size: 56px; letter-spacing: 1px; }
  .contact-brand .brand-sub { font-size: 17px; letter-spacing: 5px; margin-top: 8px; }
  .contact-panel {
    width: 58%;
    margin: 24px 0;
    background: var(--panel);
    padding: 26px 30px 22px 30px;
    display: flex;
    flex-direction: column;
  }
  .person-name { color: var(--red); font-size: 20px; }
  .person-role { color: var(--muted); font-size: 14px; margin-bottom: 16px; }
  .contact-list { list-style: none; display: flex; flex-direction: column; gap: 12px; font-size: 17px; line-height: 1.2; }
  .contact-item { display: flex; align-items: flex-start; gap: 14px; }
  .contact-icon { flex: 0 0 24px; width: 24px; height: 24px; background: var(--red); display: flex; align-items: center; justify-content: center; }
  .contact-icon svg { width: 16px; height: 16px; }
  .divider { height: 2px; background: var(--red); margin: 16px 0 14px; }
</style>
</head>
<body>

  <section class="card services" aria-label="Services side">
    <div class="brand-watermark">
      <div class="brand-name">VELKOR</div>
      <div class="brand-sub">Services Inc.</div>
    </div>
    <ul class="service-list service-list--left">
      <li>Log Book<br>Auditing</li>
      <li>Written Safety &amp;<br>Maintenance Programs</li>
      <li>Design and Printing of Log Books<br>and Trip Inspection books</li>
      <li>Compliance and<br>Audit Assistance</li>
    </ul>
    <ul class="service-list service-list--right">
      <li>Prorate<br>Licensing</li>
      <li>IFTA Fuel<br>Tax Reporting</li>
      <li>Safety Fitness<br>Certificates (SFC)</li>
      <li>Travel to<br>USA</li>
    </ul>
  </section>

  <section class="card contact" aria-label="Contact side">
    <div class="contact-brand">
      <div class="brand-name">VELKOR</div>
      <div class="brand-sub">Services Inc.</div>
    </div>
    <div class="contact-panel">
      <div class="person-name">Marek Dolan</div>
      <div class="person-role">designer</div>
      <ul class="contact-list">
        <li class="contact-item">
          <span class="contact-icon"><svg viewBox="0 0 16 16"><path d="M4 1.5l2.2 3-1.3 1.6c.8 1.8 2.2 3.2 4 4l1.6-1.3 3 2.2-1.2 2.4C7 13.2 2.8 9 1.6 2.7z" fill="#fff"/></svg></span>
          <span>Toll free<br>1-800-VELKOR (835-5671)</span>
        </li>
        <li class="contact-item">
          <span class="contact-icon"><svg viewBox="0 0 16 16"><path d="M4 1.5l2.2 3-1.3 1.6c.8 1.8 2.2 3.2 4 4l1.6-1.3 3 2.2-1.2 2.4C7 13.2 2.8 9 1.6 2.7z" fill="#fff"/></svg></span>
          <span>local<br>780-555-0142</span>
        </li>
        <li class="contact-item">
          <span class="contact-icon"><svg viewBox="0 0 16 16"><rect x="1.5" y="3.5" width="13" height="9" fill="none" stroke="#fff" stroke-width="1.4"/><path d="M1.5 3.5L8 9l6.5-5.5" fill="none" stroke="#fff" stroke-width="1.4"/></svg></span>
          <span>admin@velkor.ca</span>
        </li>
      </ul>
      <div class="divider"></div>
      <ul class="contact-list">
        <li class="contact-item">
          <span class="contact-icon"><svg viewBox="0 0 16 16"><path d="M8 1a5 5 0 0 0-5 5c0 3.6 5 9 5 9s5-5.4 5-9a5 5 0 0 0-5-5z" fill="#fff"/><circle cx="8" cy="6" r="1.8" fill="#e5262b"/></svg></span>
          <span>#310, 8240-52 Ave<br>Edmonton, Alberta<br>T6B 4K1 Canada</span>
        </li>
      </ul>
    </div>
  </section>

</body>
</html>
```